Erstellung einer ersten Einladungskarte „Safe the Date“
Zielgruppe
Spezialist für temporäres Linienmanagement & Projektmanagement
Als Sozietät für professionelles Interim Management bündelt die Lentawerk AG die fachliche Kompetenz und die langjährige Erfahrung erfolgreicher Führungspersönlichkeiten aus nahezu allen Sektoren der Wirtschaft. Wir unterstützen unsere Kunden bei der Bewältigung temporärer Herausforderungen im Linienmanagement sowie im Management komplexer strategischer Projekte und Programme.
https://www.lentawerk.example/de/home.html
Aufgabenstellung
Siehe angehängtes Briefing und angehängtes CD Manual, das nicht zwingend eingehalten werden muss für diesen Job

```html
<!DOCTYPE html>
<html lang="de">
<head>
<meta charset="utf-8">
<title>Lentawerk AG – Save the Date</title>
<link href="https://fonts.googleapis.com/css2?family=Titillium+Web:ital,wght@0,300;0,400;0,600;1,300;1,400&display=swap" rel="stylesheet">
<style>
  :root {
    --page: #ffffff;
    --card: #f6f6f5;
    --blue: #3f6888;
    --orange: #e8670c;
  }
  * { margin: 0; padding: 0; box-sizing: border-box; }
  html, body {
    width: 1200px; height: 1200px; overflow: hidden;
    background: var(--page);
    font-family: "Titillium Web", sans-serif;
    color: var(--blue);
  }
  .invitation {
    position: absolute;
    left: 54px; top: 336px;
    width: 1091px; height: 518px;
    background: var(--card);
  }
  .intro, .note {
    position: absolute;
    left: 436px;
    font-style: italic;
    font-weight: 400;
    font-size: 17px;
    line-height: 26px;
  }
  .intro { top: 88px; }
  .note { top: 316px; }
  .facts { position: absolute; left: 0; top: 145px; width: 100%; }
  .fact {
    position: absolute; left: 0;
    display: flex; align-items: baseline;
  }
  .fact-label {
    width: 413px; text-align: right;
    font-size: 16px; font-weight: 300;
  }
  .fact-value {
    margin-left: 23px;
    font-size: 25px; font-weight: 400;
  }
  .fact--when { top: 0; }
  .fact--where { top: 54px; }
  .fact--motto { top: 109px; }
  .fact--motto .fact-value { margin-left: 16px; }
  .accent { color: var(--orange); }
  .brand {
    position: absolute;
    left: 394px; top: 410px;
    font-size: 50px; font-weight: 600;
    line-height: 60px;
    color: var(--blue);
    letter-spacing: 0.5px;
  }
  .host-illustration {
    position: absolute;
    left: 814px; top: 404px;
    width: 216px; height: 114px;
    background: linear-gradient(90deg, rgba(63,104,136,0.35), var(--blue));
  }
</style>
</head>
<body>
  <section class="invitation">
    <p class="intro">Die Lentawerk AG wird 10 Jahre alt, das werden wir feiern:</p>

    <div class="facts">
      <div class="fact fact--when">
        <span class="fact-label">Wann:</span>
        <span class="fact-value">1. und 2. Dezember 2017</span>
      </div>
      <div class="fact fact--where">
        <span class="fact-label">Wo:</span>
        <span class="fact-value">München</span>
      </div>
      <div class="fact fact--motto">
        <span class="fact-label">Motto:</span>
        <span class="fact-value">„Ein Hauch von <span class="accent">Orange</span>“</span>
      </div>
    </div>

    <p class="note">Details zur Feier sowie Möglichkeiten zur Übernachtung<br>in München werden wir rechtzeitig vor der Feier mitteilen.</p>

    <div class="brand">Lentawerk</div>

    <div class="host-illustration" role="img" aria-label="Illustration: Mann im Anzug mit oranger Krawatte, der eine Geburtstagstorte mit Kerze auf einem Tablett serviert"></div>
  </section>
</body>
</html>
```